Day Spa needs attracting information signage board

Need a sign that states our name, telephone number and web address. Have a logo but not imperitave to use. Sign needs to attract clients since it's on street without many pedestrians but many cars driving by.

Target Market(s)

Females aged 18 to 60 interested in health and beauty as well as slimming. Females that want to have days off and enjoy a full day at a spa. 10% Males

Requirements
Must have
• Name - Lesedi Day Spa
Tel - 011 742 3198 / 011 657 4031
Web address: www.lesedidayspa.example.za
Address: 23 Kestrel road (with a sign showing it's around the corner)
Nice to have
• Follow us on Circlebook
Follow us on Chirpline
Services we offer
Should not have
• Should not have too bright colors that people won't be able to see in the sun.
Font should not be old-style fonts.

```html
<!DOCTYPE html>
<html lang="en">
<head>
<meta charset="utf-8">
<title>Lesedi Day Spa – Street Sign</title>
<link rel="stylesheet" href="https://fonts.googleapis.com/css2?family=PT+Sans:ital,wght@0,400;0,700;1,400&display=swap">
<style>
  :root {
    --spa-blue: #3fc6f0;
    --spa-lime: #c7d62a;
    --service-blue: #1ba6dc;
    --tag-grey: #6b6b6b;
    --ink: #1e1e1e;
    --paper: #ffffff;
    --frame: #d4d4d4;
    --social-blue: #2f4f8f;
    --social-sky: #3aa7dd;
  }
  * { margin: 0; padding: 0; box-sizing: border-box; }
  html, body { width: 1200px; height: 698px; overflow: hidden; background: var(--paper); }
  body { font-family: "PT Sans", Arial, sans-serif; color: var(--ink); }

  .sign {
    position: relative;
    width: 1200px;
    height: 698px;
    background: var(--paper);
    border: 2px solid var(--frame);
    overflow: hidden;
  }

  .product-scene {
    position: absolute;
    left: 0; top: 215px;
    width: 650px; height: 445px;
  }

  .brand-mark {
    position: absolute;
    left: 222px; top: 120px;
    width: 175px;
    text-align: center;
  }
  .brand-mark__name {
    display: flex; align-items: center; justify-content: center; gap: 6px;
    font-size: 21px; color: var(--service-blue);
  }
  .brand-mark__dot {
    width: 12px; height: 12px; border-radius: 50%; background: var(--spa-lime);
  }
  .brand-mark__tagline {
    font-size: 11px; font-style: italic; color: var(--tag-grey); margin-top: 2px;
  }

  .title-bar { position: absolute; left: 403px; top: 75px; height: 116px; display: flex; }
  .title-bar__main {
    width: 409px; background: var(--spa-blue); color: var(--paper);
    font-size: 92px; line-height: 116px; padding-left: 12px;
  }
  .title-bar__sub {
    width: 300px; background: var(--spa-lime); color: var(--paper);
    font-size: 72px; font-style: italic; line-height: 120px; padding-left: 12px;
  }

  .right-col { position: absolute; right: 82px; text-align: right; }
  .focus-areas { top: 196px; font-size: 39px; letter-spacing: 1.5px; color: var(--tag-grey); }
  .services { top: 252px; right: 78px; font-size: 33px; line-height: 44px; color: var(--service-blue); }
  .contact { top: 412px; right: 86px; font-size: 31px; line-height: 40px; color: var(--ink); }

  .social {
    position: absolute; left: 708px; top: 574px;
    display: flex; align-items: center; gap: 18px;
  }
  .social__label { font-size: 16px; font-weight: 700; line-height: 18px; text-align: right; color: var(--ink); }
  .social__item { display: flex; align-items: center; gap: 6px; font-size: 20px; }
  .social__item--circle { color: var(--social-blue); }
  .social__item--chirp { color: var(--social-sky); }
  .social__square { width: 16px; height: 16px; background: currentColor; }

  .footer-band {
    position: absolute; left: 0; bottom: 0; width: 100%; height: 40px;
    background: var(--spa-lime);
    text-align: right; padding-right: 28px;
    font-size: 23px; line-height: 40px; color: var(--ink);
  }
</style>
</head>
<body>
<main class="sign">
  <svg class="product-scene" role="img" aria-label="Spa still life: glass jug of green massage oil, bowl of green bath salts, rolled white towel and a white lily on a wooden tray" viewBox="0 0 650 445">
    <defs>
      <radialGradient id="scene-glow" cx="0.45" cy="0.65" r="0.6">
        <stop offset="0" stop-color="#e9edb0"/>
        <stop offset="0.6" stop-color="#f4f6dc"/>
        <stop offset="1" stop-color="#ffffff"/>
      </radialGradient>
    </defs>
    <rect width="650" height="445" fill="url(#scene-glow)"/>
  </svg>

  <div class="brand-mark">
    <div class="brand-mark__name"><span class="brand-mark__dot"></span>Lesedi Day Spa</div>
    <div class="brand-mark__tagline">Beauty . Health . Slimming</div>
  </div>

  <h1 class="title-bar">
    <span class="title-bar__main">Lesedi</span>
    <span class="title-bar__sub">Day Spa</span>
  </h1>

  <p class="right-col focus-areas">BEAUTY • HEALTH • SLIMMING</p>

  <p class="right-col services">
    • Spa • Massage • Body Wraps • Slimming<br>
    • Tanning • Facials • Tinting • Make-up
  </p>

  <p class="right-col contact">
    23 Kestrel road<br>
    Tel - 011 742 3198 / 657 4031
  </p>

  <div class="social">
    <p class="social__label">Stay connected<br>with us:</p>
    <span class="social__item social__item--circle"><span class="social__square"></span>Circlebook</span>
    <span class="social__item social__item--chirp"><span class="social__square"></span>Chirpline</span>
  </div>

  <footer class="footer-band">www.lesedidayspa.example.za</footer>
</main>
</body>
</html>
```